Web Design for Financial Consulting Company

We need a website design for a financial consulting company "Kelvane Consulting". We build financial models, scenario analysis, handle the budgeting process and provide temporary staffing. I have over 10 years of experience. My Excel expertise and analytical savvy has saved clients over $17 million in profit.

Target Market(s)

Small to medium businesses

Industry/Entity Type

Financial Consulting

Number of Pages Required

4 page

Requirements
Must have
• Professional looking
Nice to have
• A little futuristic looking

```html
<!DOCTYPE html>
<html lang="en">
<head>
<meta charset="utf-8">
<title>Kelvane Consulting</title>
<link href="https://fonts.googleapis.com/css2?family=Outfit:wght@400;500;600&family=Poppins:wght@400;500;600&display=swap" rel="stylesheet">
<style>
:root{
  --blue:#0fa0ef;
  --blue-soft:#e9f5fd;
  --ink:#1c1d26;
  --body:#6d7078;
  --line:#d9dce2;
  --footer:#0f4a7c;
  --footer-deep:#0b3a63;
  --white:#ffffff;
  --star:#f6b51c;
  --star-off:#c9ccd2;
}
*{margin:0;padding:0;box-sizing:border-box}
html,body{width:1200px;height:3402px;overflow:hidden}
body{position:relative;background:var(--white);font-family:"Poppins",sans-serif;color:var(--ink)}
.abs{position:absolute}
.head{font-family:"Outfit",sans-serif;font-weight:500;color:var(--ink)}
.eyebrow{font-family:"Poppins",sans-serif;font-weight:500;font-size:13px;letter-spacing:3px;color:var(--blue);text-transform:uppercase}
.rule{width:40px;height:2px;background:var(--line)}
.btn{position:absolute;background:var(--blue);color:var(--white);font-family:"Poppins",sans-serif;font-size:15px;font-weight:500;display:flex;align-items:center;justify-content:center}
.photo{position:absolute}
.copy{font-size:12.5px;line-height:24px;color:var(--body)}

/* hero */
.hero{position:absolute;left:0;top:0;width:1200px;height:650px}
.brand{position:absolute;display:flex;align-items:center;gap:10px;font-family:"Outfit",sans-serif;font-weight:600;color:var(--white);text-transform:uppercase;letter-spacing:2px}
.brand-mark{border:3px solid var(--blue)}
.nav{position:absolute;top:27px;font-size:15px;color:var(--white)}
.nav.active{color:var(--blue)}
.hero-title{position:absolute;left:161px;top:186px;font-family:"Outfit",sans-serif;font-weight:500;font-size:47px;line-height:58px;color:var(--white);letter-spacing:.5px}

/* services */
.services-bg{position:absolute;left:0;top:1135px;width:1200px;height:600px;background:linear-gradient(180deg,#f5f9fd 0%,#eef5fc 70%,#ffffff 100%)}
.service-card{position:absolute;top:1340px;width:277px;height:317px;background:var(--white);box-shadow:0 4px 18px rgba(20,60,110,.07);border-bottom:4px solid var(--blue)}
.service-card .icon{position:absolute;left:70px;top:30px}
.service-card .num{position:absolute;left:21px;top:97px;font-family:"Outfit",sans-serif;font-size:25px;font-weight:500;color:var(--blue)}
.service-card .dash{position:absolute;left:54px;top:112px;width:12px;height:1px;background:var(--line)}
.service-card .title{position:absolute;left:71px;top:100px;font-family:"Outfit",sans-serif;font-size:17px;line-height:20px;font-weight:500;color:var(--ink)}
.service-card .copy{position:absolute;left:70px;top:150px;width:196px}

/* reviews */
.review-card{position:absolute;width:277px;height:261px;background:var(--white);box-shadow:0 4px 22px rgba(20,40,80,.09)}
.review-card .avatar{position:absolute;left:20px;top:22px;width:60px;height:60px;border-radius:50%}
.review-card .quote{position:absolute;right:26px;top:4px;font-family:"Outfit",sans-serif;font-size:90px;line-height:90px;color:#d3e9f8}
.review-card .rule-in{position:absolute;left:20px;top:100px;width:237px;height:1px;background:#eef0f3}
.review-card .copy{position:absolute;left:20px;top:112px;width:240px;font-size:12.5px;line-height:20px;color:#3a3c45}
.review-card .name{position:absolute;left:20px;top:200px;font-size:12.5px;font-weight:500;color:var(--ink)}
.review-card .stars{position:absolute;left:28px;top:222px}
.arrow-btn{position:absolute;top:1900px;width:40px;height:37px;display:flex;align-items:center;justify-content:center}

/* blogs */
.blogs-bg{position:absolute;left:0;top:2345px;width:1200px;height:672px;background:#f7f8fa}
.blog{position:absolute;top:2488px;width:279px}
.blog .thumb{position:relative;width:279px;height:201px}
.blog .title{margin-top:12px;font-family:"Outfit",sans-serif;font-size:16px;line-height:23px;font-weight:500;color:var(--ink)}
.blog .copy{margin-top:3px;font-size:12px;line-height:20px;color:#3d3f47}
.blog .author{margin-top:14px;display:flex;align-items:center;gap:16px}
.blog .author-pic{width:36px;height:36px;border-radius:50%}
.blog .author-name{font-size:12.5px;font-weight:500;color:var(--ink)}
.blog .author-role{font-size:10.5px;color:#555862;margin-top:2px}

/* footer */
.footer{position:absolute;left:0;top:3016px;width:1200px;height:386px;background:linear-gradient(100deg,var(--footer-deep) 0%,var(--footer) 55%,#14588f 100%);color:var(--white)}
.footer-head{position:absolute;font-size:15px;color:var(--blue);font-weight:500;display:flex;align-items:center;gap:8px}
.footer-head::before{content:"";width:18px;height:1px;background:var(--blue)}
.footer-text{position:absolute;font-size:11.5px;line-height:20px;color:#e4edf6}
.social{position:absolute;top:3255px;width:36px;height:36px;border:1px solid rgba(255,255,255,.55);display:flex;align-items:center;justify-content:center}
.social span{width:8px;height:8px;background:var(--white);border-radius:50%}
</style>
</head>
<body>

<!-- HERO -->
<section class="hero">
  <svg width="1200" height="650" viewBox="0 0 1200 650" class="abs" style="left:0;top:0">
    <defs>
      <linearGradient id="heroShade" x1="0" y1="0" x2="1" y2="0.4">
        <stop offset="0" stop-color="#2d3a46"/>
        <stop offset=".45" stop-color="#55626d"/>
        <stop offset="1" stop-color="#8a949c"/>
      </linearGradient>
    </defs>
    <polygon points="0,0 1200,0 1200,512 865,636 0,500" fill="url(#heroShade)" role="img" aria-label="Three colleagues reviewing results on a tablet in a bright office"/>
    <polygon points="0,500 865,636 1200,512 1200,520 865,650 0,505" fill="var(--blue)"/>
  </svg>
  <div class="brand" style="left:161px;top:18px">
    <span class="brand-mark" style="width:34px;height:34px"></span>
    <span style="font-size:20px;line-height:22px">Kelvane Consulting</span>
  </div>
  <span class="nav active" style="left:577px">Home</span>
  <span class="nav" style="left:661px">About</span>
  <span class="nav" style="left:744px">Services</span>
  <span class="nav" style="left:846px">Team</span>
  <div class="btn" style="left:927px;top:18px;width:112px;height:36px;font-size:14px">Contact</div>
  <h1 class="hero-title">Our Target Are<br>Small To Medium<br>Businesses</h1>
  <div class="btn" style="left:161px;top:380px;width:121px;height:40px;font-size:14px">Contact Us</div>
</section>

<!-- ABOUT -->
<section>
  <div class="abs" style="left:92px;top:702px;width:164px;height:164px;border:9px solid var(--blue)"></div>
  <div class="photo" role="img" aria-label="Smiling consultant with arms crossed in a meeting room" style="left:276px;top:682px;width:313px;height:265px;background:linear-gradient(160deg,#c9b9a5,#8f8476 60%,#5d5a58)"></div>
  <div class="photo" role="img" aria-label="Team collaborating around a laptop" style="left:169px;top:887px;width:199px;height:180px;background:linear-gradient(150deg,#8a6e52,#4f4236 70%,#2f2a26);border-top:6px solid #fff;border-right:6px solid #fff"></div>
  <div class="abs head" style="left:394px;top:966px;font-size:58px;line-height:60px;color:var(--blue)">10<span style="font-size:38px;color:var(--ink)">Years</span></div>
  <div class="abs" style="left:403px;top:1032px;font-size:15px;letter-spacing:4px;color:var(--blue)">Of Experience</div>

  <div class="abs eyebrow" style="left:624px;top:715px">About Us</div>
  <h2 class="abs head" style="left:624px;top:738px;font-size:29px">Who We Are</h2>
  <div class="abs rule" style="left:624px;top:782px"></div>
  <p class="abs" style="left:624px;top:799px;width:408px;font-size:12.5px;line-height:24.5px;font-weight:500;color:var(--ink)">I am an experienced Finance professional who develops strategic financial plans, provides insightful analysis, and supports decision – making. With over 10 years of experience, I have successfully increased profitability for clients by $17M.</p>
  <p class="abs copy" style="left:624px;top:903px;width:410px">Lorem ipsum dolor sit amet, consetetur sadipscing elitr, sed diam nonumy eirmod tempor invidunt ut labore et dolore magna aliquyam erat, sed diam voluptua.</p>
  <div class="btn" style="left:624px;top:989px;width:113px;height:37px;font-size:14px">Read More</div>
</section>

<!-- SERVICES -->
<section>
  <div class="services-bg"></div>
  <div class="abs eyebrow" style="left:199px;top:1221px">Our Services</div>
  <h2 class="abs head" style="left:199px;top:1240px;font-size:29px">Financial Models</h2>
  <div class="abs rule" style="left:199px;top:1286px"></div>
  <h3 class="abs" style="left:479px;top:1203px;font-size:14.5px;font-weight:500;color:var(--ink)">Lorem ipsum dolor sit amet, consectetuer adipiscing elit</h3>
  <p class="abs copy" style="left:479px;top:1234px;width:540px">Lorem ipsum dolor sit amet, consetetur sadipscing elitr, sed diam nonumy eirmod tempor invidunt ut labore et dolore magna aliquyam erat, sed diam voluptua.orem ipsum dolor sit amet, consetetur sadipscing elitr, sed diam nonumy...</p>

  <svg class="abs" style="left:105px;top:1490px" width="26" height="16" viewBox="0 0 26 16"><path d="M25 8H2M9 1L2 8l7 7" fill="none" stroke="var(--ink)" stroke-width="1.8"/></svg>
  <svg class="abs" style="left:1074px;top:1490px" width="26" height="16" viewBox="0 0 26 16"><path d="M1 8h23M17 1l7 7-7 7" fill="none" stroke="var(--blue)" stroke-width="1.8"/></svg>

  <article class="service-card" style="left:161px">
    <svg class="icon" width="48" height="50" viewBox="0 0 48 50" fill="none" stroke="var(--ink)" stroke-width="1.6"><rect x="3" y="2" width="26" height="34"/><path d="M8 9h14M8 14h10M8 19h8"/><circle cx="30" cy="32" r="9" stroke="var(--blue)"/><path d="M36.5 38.5L44 46"/><path d="M3 44h24"/></svg>
    <span class="num">01</span><span class="dash"></span>
    <h3 class="title">Scenario<br>Analysis</h3>
    <p class="copy">Lorem ipsum dolor sit amet, consetetur sadipscing elitr, sed diam nonumy eirmod tempor invidunt ut labore et dolore magna aliquyam erat...</p>
  </article>
  <article class="service-card" style="left:461px">
    <svg class="icon" width="52" height="50" viewBox="0 0 52 50" fill="none" stroke="var(--ink)" stroke-width="1.6"><circle cx="18" cy="30" r="8"/><circle cx="18" cy="30" r="13" stroke-dasharray="4 3"/><circle cx="34" cy="16" r="5" stroke="var(--blue)"/><circle cx="44" cy="8" r="6"/><path d="M41 8l2 2 4-4" stroke="var(--blue)"/></svg>
    <span class="num">02</span><span class="dash"></span>
    <h3 class="title">Handle The<br>Budgeting Process</h3>
    <p class="copy">Lorem ipsum dolor sit amet, consetetur sadipscing elitr, sed diam nonumy eirmod tempor invidunt ut labore et dolore magna aliquyam erat...</p>
  </article>
  <article class="service-card" style="left:762px">
    <svg class="icon" width="52" height="52" viewBox="0 0 52 52" fill="none" stroke="var(--ink)" stroke-width="1.6"><circle cx="14" cy="26" r="8"/><circle cx="14" cy="26" r="3" stroke="var(--blue)"/><path d="M24 26h8M32 10v32"/><circle cx="42" cy="8" r="4" stroke="var(--blue)"/><path d="M36 20a6 6 0 0112 0"/><rect x="37" y="36" width="10" height="12" stroke="var(--blue)"/></svg>
    <span class="num">03</span><span class="dash"></span>
    <h3 class="title">Provide<br>Temporary Staffing.</h3>
    <p class="copy">Lorem ipsum dolor sit amet, consetetur sadipscing elitr, sed diam nonumy eirmod tempor invidunt ut labore et dolore magna aliquyam erat...</p>
  </article>
</section>

<!-- REVIEWS -->
<section>
  <div class="abs eyebrow" style="left:0;width:1200px;text-align:center;top:1815px">Client Reviews</div>
  <h2 class="abs head" style="left:0;width:1200px;text-align:center;top:1834px;font-size:29px">What Our Clients say</h2>
  <div class="abs rule" style="left:580px;top:1880px"></div>
  <p class="abs copy" style="left:330px;top:1897px;width:540px;text-align:center;color:#3d3f47">Lorem ipsum dolor sit amet, consetetur sadipscing elitr, sed diam nonumy eirmod ipsum dolor sit amet, consetetur sadipscing elitr, sed diam nonumy...</p>
  <div class="arrow-btn" style="left:956px;background:#eef0f3"><svg width="22" height="14" viewBox="0 0 22 14"><path d="M21 7H2M8 1L2 7l6 6" fill="none" stroke="var(--ink)" stroke-width="1.7"/></svg></div>
  <div class="arrow-btn" style="left:999px;background:var(--blue)"><svg width="22" height="14" viewBox="0 0 22 14"><path d="M1 7h19M14 1l6 6-6 6" fill="none" stroke="#fff" stroke-width="1.7"/></svg></div>

  <article class="review-card" style="left:-140px;top:1930px;opacity:.9">
    <span class="quote" style="right:26px">”</span><span class="rule-in"></span>
    <p class="copy" style="left:142px;top:110px">sit amet,<br>ing elitr, sed diam<br>mpor invidunt ut</p>
    <span class="name" style="left:142px;top:205px">or sit</span>
  </article>

  <article class="review-card" style="left:161px;top:1976px">
    <div class="avatar" role="img" aria-label="Client portrait" style="background:linear-gradient(150deg,#3c5f86,#1f2f44)"></div>
    <span class="quote">”</span><span class="rule-in"></span>
    <p class="copy">Lorem ipsum dolor sit amet, consetetur sadipscing elitr, sed diam nonumy eirmod tempor invidunt ut labore et dolore...</p>
    <span class="name">– Lorem ipsum dolor sit</span>
    <svg class="stars" width="92" height="16" viewBox="0 0 92 16"><g id="star4"><polygon points="8,0 10.4,5.3 16,5.8 11.8,9.5 13,15 8,12.1 3,15 4.2,9.5 0,5.8 5.6,5.3" fill="var(--star)"/><polygon transform="translate(19 0)" points="8,0 10.4,5.3 16,5.8 11.8,9.5 13,15 8,12.1 3,15 4.2,9.5 0,5.8 5.6,5.3" fill="var(--star)"/><polygon transform="translate(38 0)" points="8,0 10.4,5.3 16,5.8 11.8,9.5 13,15 8,12.1 3,15 4.2,9.5 0,5.8 5.6,5.3" fill="var(--star)"/><polygon transform="translate(57 0)" points="8,0 10.4,5.3 16,5.8 11.8,9.5 13,15 8,12.1 3,15 4.2,9.5 0,5.8 5.6,5.3" fill="var(--star)"/><polygon transform="translate(76 0)" points="8,0 10.4,5.3 16,5.8 11.8,9.5 13,15 8,12.1 3,15 4.2,9.5 0,5.8 5.6,5.3" fill="var(--star-off)"/></g></svg>
  </article>

  <article class="review-card" style="left:461px;top:1996px">
    <div class="avatar" role="img" aria-label="Client portrait" style="background:linear-gradient(150deg,#e2c2a8,#9b6f55)"></div>
    <span class="quote">”</span><span class="rule-in"></span>
    <p class="copy">Lorem ipsum dolor sit amet, consetetur sadipscing elitr, sed diam nonumy eirmod tempor invidunt ut labore et dolore...</p>
    <span class="name">– Lorem ipsum dolor sit</span>
    <svg class="stars" width="92" height="16" viewBox="0 0 92 16"><use href="#star4"/></svg>
  </article>

  <article class="review-card" style="left:761px;top:1976px">
    <div class="avatar" role="img" aria-label="Client portrait" style="background:linear-gradient(150deg,#8d7564,#3f3833)"></div>
    <span class="quote">”</span><span class="rule-in"></span>
    <p class="copy">Lorem ipsum dolor sit amet, consetetur sadipscing elitr, sed diam nonumy eirmod tempor invidunt ut labore et dolore...</p>
    <span class="name">– Lorem ipsum dolor sit</span>
    <svg class="stars" width="92" height="16" viewBox="0 0 92 16"><use href="#star4"/></svg>
  </article>

  <article class="review-card" style="left:1056px;top:1936px;opacity:.75">
    <div class="avatar" role="img" aria-label="Client portrait" style="left:21px;background:linear-gradient(150deg,#c79c82,#5d3f31)"></div>
    <p class="copy" style="left:20px;top:110px;width:250px">Lorem ipsum dolor sit amet, consetetur sadipscing elitr, nonumy eirmod tempor labore et dolore...</p>
    <span class="name" style="top:196px">– Lorem ipsum dolor sit</span>
    <svg class="stars" style="top:218px" width="92" height="16" viewBox="0 0 92 16"><use href="#star4"/></svg>
  </article>
</section>

<!-- BLOGS -->
<section>
  <div class="blogs-bg"></div>
  <h2 class="abs head" style="left:0;width:1200px;text-align:center;top:2410px;font-size:29px">Our Latest Blogs</h2>
  <div class="abs rule" style="left:580px;top:2456px"></div>

  <article class="blog" style="left:161px">
    <div class="thumb" role="img" aria-label="Hands signing financial paperwork beside glasses" style="background:linear-gradient(135deg,#e9d6b3,#c9a97c 45%,#e6e8ec)"></div>
    <h3 class="title">Lorem ipsum dolor sit amet, co setetur sadipscing elit...</h3>
    <p class="copy">Lorem Ipsum is simply dummy text of the prin ting and typesetting industry Lorem Ipsum has been the industry.</p>
    <div class="author"><div class="author-pic" role="img" aria-label="Author portrait" style="background:linear-gradient(150deg,#b88a6e,#4e3328)"></div><div><div class="author-name">Lorem ipsum dolor sit</div><div class="author-role">Ipsum Lorem simply...</div></div></div>
  </article>
  <article class="blog" style="left:463px">
    <div class="thumb" role="img" aria-label="Presenter beside market charts in a boardroom" style="background:linear-gradient(135deg,#f0f2f5,#b9c3cf 50%,#58606b)"></div>
    <h3 class="title">Lorem ipsum dolor sit amet, co setetur sadipscing elit...</h3>
    <p class="copy">Lorem Ipsum is simply dummy text of the prin ting and typesetting industry Lorem Ipsum has been the industry.</p>
    <div class="author"><div class="author-pic" role="img" aria-label="Author portrait" style="background:linear-gradient(150deg,#c7c9cf,#4d535c)"></div><div><div class="author-name">Lorem ipsum dolor sit</div><div class="author-role">Ipsum Lorem simply...</div></div></div>
  </article>
  <article class="blog" style="left:766px">
    <div class="thumb" role="img" aria-label="Two businessmen reviewing a document together" style="background:linear-gradient(135deg,#34506f,#7f95ab 55%,#d6dde5)"></div>
    <h3 class="title">Lorem ipsum dolor sit amet, co setetur sadipscing elit...</h3>
    <p class="copy">Lorem Ipsum is simply dummy text of the prin ting and typesetting industry Lorem Ipsum has been the industry.</p>
    <div class="author"><div class="author-pic" role="img" aria-label="Author portrait" style="background:linear-gradient(150deg,#d4c7b6,#6f6356)"></div><div><div class="author-name">Lorem ipsum dolor sit</div><div class="author-role">Ipsum Lorem simply...</div></div></div>
  </article>

  <div class="btn" style="left:540px;top:2909px;width:113px;height:37px;font-size:14px">View All</div>
</section>

<!-- FOOTER -->
<footer class="footer" role="img" aria-label="Footer backdrop of city towers tinted blue"></footer>
<div class="brand" style="left:161px;top:3076px">
  <span class="brand-mark" style="width:40px;height:40px"></span>
  <span style="font-size:24px;line-height:26px">Kelvane Consulting</span>
</div>
<p class="footer-text" style="left:161px;top:3132px;width:270px">Lorem Ipsum is simply dummy text of the prin ting and typesetting industry Lorem Ipsum has been the industry.Lorem Ipsum is of the prin ting and typesetting industry Lorem Ipsum has been the industry.</p>
<div class="social" style="left:161px" aria-label="Social link one"><span></span></div>
<div class="social" style="left:207px" aria-label="Social link two"><span></span></div>
<div class="social" style="left:252px" aria-label="Social link three"><span></span></div>
<div class="social" style="left:298px" aria-label="Social link four"><span></span></div>
<div class="social" style="left:344px" aria-label="Social link five"><span></span></div>

<div class="footer-head" style="left:495px;top:3110px">Contact</div>
<svg class="abs" style="left:494px;top:3163px" width="14" height="18" viewBox="0 0 14 18"><path d="M7 17s6-6 6-10A6 6 0 001 7c0 4 6 10 6 10z" fill="none" stroke="var(--blue)" stroke-width="1.4"/><circle cx="7" cy="7" r="2" fill="none" stroke="var(--blue)" stroke-width="1.4"/></svg>
<p class="footer-text" style="left:527px;top:3162px;line-height:16px;font-size:11px">123 Street Name<br>Texas, USA</p>
<svg class="abs" style="left:494px;top:3203px" width="15" height="15" viewBox="0 0 15 15"><path d="M3 1l3 3-2 2a9 9 0 005 5l2-2 3 3-2 2C6 14 1 9 1 3z" fill="none" stroke="var(--blue)" stroke-width="1.3"/></svg>
<p class="footer-text" style="left:527px;top:3201px;font-size:11px">1-234-567-8901</p>
<svg class="abs" style="left:494px;top:3238px" width="16" height="12" viewBox="0 0 16 12"><rect x="1" y="1" width="14" height="10" fill="none" stroke="var(--blue)" stroke-width="1.3"/><path d="M1 1l7 6 7-6" fill="none" stroke="var(--blue)" stroke-width="1.3"/></svg>
<p class="footer-text" style="left:527px;top:3234px;font-size:11px">info@kelvane.com</p>

<div class="footer-head" style="left:690px;top:3110px">Links</div>
<p class="footer-text" style="left:692px;top:3146px;font-size:11px;line-height:28.6px">Home<br>About<br>Services<br>Team<br>Contact</p>

<div class="footer-head" style="left:810px;top:3110px">Subscribe</div>
<p class="footer-text" style="left:811px;top:3148px;width:230px;font-size:12px;line-height:18px">Subscribe to our newsletter to get our latest update &amp; news.</p>
<div class="abs" style="left:810px;top:3196px;width:196px;height:32px;background:var(--footer-deep);font-size:10.5px;color:#e4edf6;padding:9px 16px">Your email</div>
<div class="abs" style="left:1006px;top:3196px;width:33px;height:32px;background:var(--blue);display:flex;align-items:center;justify-content:center"><svg width="18" height="16" viewBox="0 0 18 16"><path d="M1 7l16-6-5 14-3-6zM9 9l8-8" fill="none" stroke="#fff" stroke-width="1.4"/></svg></div>

<p class="abs" style="left:0;width:1200px;top:3362px;text-align:center;font-size:11px;font-weight:500;color:var(--white)">© 2021 Brightmoor Financial Group. All Rights Reserved.</p>

</body>
</html>
```